Modern Web Design for Nonprofit Organization

Our client is looking to redesign their website. They want a modern look, clean and professional, that integrates their new brand guidelines.

Here is clients current site:
http://www.valorandes.org/

They want their own unique design but here are some sites the clients likes:
https://www.brixtonvane.com/en/
https://oakhollowrise.org/
https://www.lumacraft.com/
https://www.tbnlawgroup.com/
https://www.greyharborco.org/

Attached please find the clients logos, color palette, site plan and design specs.

You will create a homepage mockup that will have the following sections in this order:
1. Thin Alert Bar at very top with one line message
2. Nav Bar with Logo and Main Nav (red in site plan)
3. Hero Image or Video
4. Signup Bar with name email and zip and connect button
5. Intro section with image, welcome message, and supporter counter
6. Featured Action section with call to action
7. Event section with two upcoming event cards
8. Latest News section with three latest blog post
9. Support our work (donation) section
10. Worker and Member Stories Section with feed of social posts
11. Footer.

You can use text and images from clients existing site or placeholder images and placeholder text.

Please submit as many home page mockups/idea boards as you like. Client will pick the top three and ask for some revisions. If you are selected this will lead to a lot of work for this client.

Project is private please adhere to ArtPlenary terms of use and do not share any materials please.

QUICKEST RESPONSE PLEASE!

Thanks for looking!

Target Market(s)

Non profit donors and farmworker advocates

Number of Pages Required

2 page

Font styles to use
Sans Serif

Requirements
Must have
• Adhere to brief and client brand ID
Nice to have
• World class design

```html
<!DOCTYPE html>
<html lang="en">
<head>
<meta charset="utf-8">
<title>Fieldhand Foundation</title>
<link rel="stylesheet" href="https://fonts.googleapis.com/css2?family=Montserrat:wght@400;500;600;700&family=Open+Sans:wght@400;600&display=swap">
<style>
:root{
  --teal:#5cc6cc;
  --teal-dark:#4fb9c0;
  --yellow:#ffd000;
  --ink:#1f1f1f;
  --body:#3a3a3a;
  --muted:#9a9a9a;
  --violet:#8c7cf0;
  --grey-band:#f7f7f7;
  --white:#fff;
  --dot-tint:#f1eefd;
}
*{box-sizing:border-box;margin:0;padding:0}
html,body{width:1200px;height:5357px;overflow:hidden}
body{position:relative;font-family:"Open Sans",Arial,sans-serif;color:var(--body);background:var(--white)}
.abs{position:absolute}
h2.section-title{position:absolute;left:0;width:1200px;text-align:center;font:700 22px "Montserrat",sans-serif;color:var(--ink);letter-spacing:.5px}
.underline{position:absolute;left:573px;width:54px;height:2px;background:var(--yellow)}
.btn{position:absolute;background:var(--yellow);display:flex;align-items:center;justify-content:center;font:600 15px "Montserrat",sans-serif;color:var(--ink);letter-spacing:.5px}
p.copy{font-size:13px;line-height:27px}

/* hero */
.hero{position:absolute;left:0;top:0;width:1200px;height:676px;background:var(--teal)}
.alert{position:absolute;left:76px;top:14px;font:600 11px "Montserrat",sans-serif;color:#fff}
.top-donate{position:absolute;left:1035px;top:9px;width:96px;height:28px;border:2px solid #fff;color:#fff;font:500 15px "Montserrat",sans-serif;display:flex;align-items:center;justify-content:center}
.brand{position:absolute;left:73px;top:66px;display:flex;align-items:center;gap:8px;color:#fff;font:700 12px/13px "Montserrat",sans-serif}
.brand .dot{width:36px;height:36px;border-radius:50%;background:#fff}
.nav{position:absolute;left:450px;top:86px;display:flex;gap:30px;font:600 11px "Montserrat",sans-serif;color:#fff}
.hero-photo{position:absolute;left:120px;top:165px;width:440px;height:380px;border-radius:6px;background:radial-gradient(ellipse at 50% 50%,#b14a8a 0%,#7a3b86 35%,#6cbfc5 75%,var(--teal) 100%)}
.signup{position:absolute;left:718px;top:141px;width:410px;height:469px;background:#fff;box-shadow:0 8px 24px rgba(0,0,0,.15)}
.signup-head{height:115px;background:var(--yellow);padding:26px 0 0 68px}
.signup-head h3{font:600 17px "Montserrat",sans-serif;color:var(--ink)}
.signup-head p{font-size:12px;line-height:21px;color:#6c5a00;margin-top:12px;width:200px}
.field{position:absolute;left:68px;width:282px;height:54px;border:1px solid #c9c9c9;border-radius:8px;padding-left:40px;display:flex;align-items:center;font-size:13px;color:var(--muted)}
.signup .btn{left:68px;top:377px;width:282px;height:54px;border-radius:8px;font-size:14px}

/* welcome */
.welcome-back{left:227px;top:853px;width:351px;height:231px;background:var(--yellow)}
.welcome-photo{left:158px;top:792px;width:395px;height:248px;background:linear-gradient(135deg,#6b7a3c,#8a6b50 45%,#d84040 60%,#5d6e3a)}
.welcome-title{left:709px;top:790px;font:700 25px "Montserrat",sans-serif;color:var(--ink)}
.welcome-text{left:709px;top:848px;width:370px}
.counter-ring{left:697px;top:1013px;width:125px;height:125px;border-radius:50%;background:#fdf3d2}
.counter{left:697px;top:1048px;font:700 27px "Montserrat",sans-serif;color:#a0a0a0}
.counter-sub{left:709px;top:1090px;font:700 15px "Montserrat",sans-serif;color:var(--ink)}

/* features */
.features-band{left:0;top:1379px;width:1200px;height:514px;background:var(--grey-band)}
.feature{position:absolute;top:1450px;width:290px;text-align:center}
.feature svg{display:block;margin:0 auto}
.feature h4{margin-top:34px;font:600 21px "Montserrat",sans-serif;color:var(--violet)}
.feature p{margin-top:20px;font-size:12.5px;line-height:27px}

/* events */
.event{position:absolute;top:2121px;width:302px;height:360px;background:#fff;box-shadow:0 3px 14px rgba(0,0,0,.12)}
.event .img{height:160px}
.event .tag{position:absolute;right:36px;top:-18px;background:#f5a623;color:#fff;font:500 11px "Montserrat",sans-serif;padding:8px 10px}
.event h4{text-align:center;font:600 14px "Montserrat",sans-serif;color:var(--ink);margin-top:25px}
.event .meta{padding-left:38px;margin-top:12px;font-size:14px;line-height:30px;color:#777}
.event .meta span{display:inline-block;width:24px;color:#333}
.event .foot{position:absolute;left:0;bottom:0;width:100%;height:46px;border-top:1px solid #eee;display:flex;align-items:center;justify-content:center;font:500 15px "Montserrat",sans-serif;color:var(--ink)}

/* blog */
.post{position:absolute;left:40px;width:1118px;height:225px;background:#fff;box-shadow:0 3px 16px rgba(0,0,0,.1)}
.post .img{position:absolute;left:72px;top:43px;width:167px;height:144px}
.post h4{position:absolute;left:297px;top:38px;width:640px;font:600 14px/29px "Montserrat",sans-serif;color:var(--ink)}
.post p{position:absolute;left:297px;top:110px;width:640px;font-size:12px;line-height:27px}
.post .more{position:absolute;left:960px;top:100px;width:104px;height:40px;background:var(--yellow);color:#fff;font:600 11px "Montserrat",sans-serif;display:flex;align-items:center;justify-content:center}
.post .date{position:absolute;left:968px;top:170px;font-size:14px;color:#888}

/* support */
.dots-area{left:94px;top:3592px;width:230px;height:135px;background:var(--dot-tint);border-radius:4px}
.support-title{left:98px;top:3790px;font:600 21px "Montserrat",sans-serif;color:var(--ink)}
.support-text{left:98px;top:3838px;width:380px}
.share{left:310px;top:3972px;font-size:13px;color:var(--ink);display:flex;align-items:center;gap:14px}
.share b{font-weight:600;color:#2b7bd9;font-size:12px}
.support-art{left:530px;top:3661px;width:576px;height:426px;border-radius:45% 55% 40% 60%;background:radial-gradient(ellipse at 40% 55%,#8c7cf0 0%,#f4d8ef 45%,#fdf0f7 80%,#fff 100%)}

/* stories */
.stories{left:0;top:4222px;width:1200px;height:761px;background:var(--yellow);overflow:hidden}
.stories h3{position:absolute;left:0;top:106px;width:1200px;text-align:center;font:500 19px "Montserrat",sans-serif;color:#fff}
.story{position:absolute;top:223px;background:#fff;height:314px;box-shadow:0 4px 16px rgba(0,0,0,.08)}
.story .avatar{position:absolute;left:44px;top:36px;width:82px;height:82px;border-radius:50%;background:linear-gradient(135deg,#e8c5a8,#a06a50)}
.story .name{position:absolute;left:148px;top:54px;font:600 14px "Montserrat",sans-serif;color:var(--ink)}
.story .ago{position:absolute;left:148px;top:80px;font-size:12px;color:#bbb}
.story .bm{position:absolute;right:40px;top:38px;width:18px;height:24px;border:2px solid #ccc;border-bottom:none}
.story p{position:absolute;left:44px;top:150px;width:380px;font-size:12px;line-height:27px}
.story .loc{position:absolute;left:44px;bottom:28px;font-size:14px;color:var(--violet)}
.story .loc b{color:var(--ink);margin-right:10px}
.story .likes{position:absolute;right:48px;bottom:28px;font-size:13px;color:#aaa}
.pager{position:absolute;top:612px;left:556px;display:flex;gap:15px}
.pager i{width:18px;height:18px;border-radius:50%;border:2px solid #fff;display:block}
.pager i.on{background:#fff}

/* footer */
.footer{left:0;top:4983px;width:1200px;height:374px;background:linear-gradient(180deg,var(--teal),var(--teal-dark))}
.foot-brand{position:absolute;left:125px;top:52px;display:flex;align-items:center;gap:8px;color:rgba(255,255,255,.7);font:600 13px/14px "Montserrat",sans-serif}
.foot-brand .dot{width:34px;height:34px;border-radius:50%;background:rgba(255,255,255,.5)}
.social{position:absolute;top:62px;width:120px;text-align:center;font:600 11px "Montserrat",sans-serif;color:#fff}
.foot-donate{position:absolute;left:907px;top:40px;width:104px;height:37px;border:2px solid #fff;color:#fff;font:500 11px "Montserrat",sans-serif;display:flex;align-items:center;justify-content:center}
.foot-links{position:absolute;left:0;top:214px;width:1200px;display:flex;justify-content:center;gap:68px;font:600 11px "Montserrat",sans-serif;color:#fff}
.copyright{position:absolute;left:0;top:318px;width:1200px;text-align:center;font-size:11px;color:#fff}
</style>
</head>
<body>

<section class="hero">
  <div class="alert">1-800-555-0142 Regional Offices</div>
  <div class="top-donate">Donate</div>
  <div class="brand"><span class="dot"></span><span>FIELDHAND<br>FOUNDATION</span></div>
  <nav class="nav"><span>GET HELP NOW ▾</span><span>TAKE ACTION ▾</span><span>NEWS &amp; EVENTS ▾</span><span>SUPPORT OUR WORK ▾</span><span>ABOUT US ▾</span></nav>
  <div class="hero-photo" role="img" aria-label="Smiling child in a superhero costume bursting through paper"></div>
  <form class="signup">
    <div class="signup-head"><h3>Sign Up Now!</h3><p>Create your account now with less information.</p></div>
    <div class="field" style="top:152px">Name</div>
    <div class="field" style="top:226px">Email</div>
    <div class="field" style="top:301px">zip Code</div>
    <div class="btn">SUBMIT</div>
  </form>
</section>

<div class="abs welcome-back"></div>
<div class="abs welcome-photo" role="img" aria-label="Farm worker in a red shirt in a vineyard"></div>
<h2 class="abs welcome-title">WELCOME</h2>
<p class="abs copy welcome-text">Lorem ipsum dolor sit amet, consetetur sadipscing elitr, sed diam nonumy eirmod tempor invidunt ut labore et dolore magna aliquyam erat, sed diam voluptua. At vero eos et accusam et justo duo dolores et ea rebum. Stet clita kasd gubergren, no sea takimata sanctus est Lorem ipsum</p>
<div class="abs counter-ring"></div>
<div class="abs counter">+150,150 SUPPORTER</div>
<div class="abs counter-sub">ACROSS THE USA</div>

<h2 class="section-title" style="top:1252px">OUR FEATURES</h2>
<div class="underline" style="top:1302px"></div>
<p class="abs" style="left:0;width:1200px;text-align:center;top:1324px;font-size:13px">Lorem ipsum dolor sit amet, consetetur</p>

<div class="abs features-band"></div>
<div class="feature" style="left:150px">
  <svg width="60" height="64" viewBox="0 0 60 64" fill="none" stroke="#8c7cf0" stroke-width="2"><path d="M30 4 56 18v28L30 60 4 46V18z"/><path d="M4 18l26 14 26-14M30 32v28"/></svg>
  <h4>Products</h4><p>Lorem ipsum dolor sit amet, consetetur sadipscing elitr, sed diam nonumy eirmod tempor invidunt ut labore et dolore magna</p>
</div>
<div class="feature" style="left:465px">
  <svg width="60" height="64" viewBox="0 0 60 64" fill="none" stroke="#8c7cf0" stroke-width="2"><circle cx="30" cy="18" r="13"/><rect x="8" y="38" width="44" height="22" rx="11"/></svg>
  <h4>Employee</h4><p>Lorem ipsum dolor sit amet, consetetur sadipscing elitr, sed diam nonumy eirmod tempor invidunt ut labore et dolore magna</p>
</div>
<div class="feature" style="left:758px">
  <svg width="60" height="64" viewBox="0 0 60 64" fill="none" stroke="#8c7cf0" stroke-width="2"><path d="M10 30a20 20 0 0 1 36-10M50 34a20 20 0 0 1-36 10"/><path d="M46 10v10H36M14 54V44h10"/></svg>
  <h4>Processes</h4><p>Lorem ipsum dolor sit amet, consetetur sadipscing elitr, sed diam nonumy eirmod tempor invidunt ut labore et dolore magna</p>
</div>
<div class="btn" style="left:505px;top:1749px;width:188px;height:58px">CALL US</div>

<h2 class="section-title" style="top:1961px">UPCOMING EVENTS</h2>
<div class="underline" style="top:2013px"></div>

<article class="event" style="left:112px">
  <div class="img" role="img" aria-label="Crowd gathered at an outdoor community event" style="background:linear-gradient(135deg,#3b6a2f,#c9433a 50%,#2e3d55)"></div>
  <span class="tag">UPCOMING</span>
  <h4>20MARH</h4>
  <div class="meta"><div><span>⚲</span>Riverton, 48 Cedar Lane, USA</div><div><span>▦</span>20/12/2020</div></div>
  <div class="foot">event information</div>
</article>
<article class="event" style="left:449px">
  <div class="img" role="img" aria-label="Audience seated in a conference hall facing a screen" style="background:linear-gradient(180deg,#6e7378,#2d3136)"></div>
  <span class="tag">UPCOMING</span>
  <h4>IMMEGRANT CONFERENCE</h4>
  <div class="meta"><div><span>⚲</span>Riverton, 48 Cedar Lane, USA</div><div><span>▦</span>20/11/2020</div></div>
  <div class="foot">event information</div>
</article>
<article class="event" style="left:786px">
  <div class="img" role="img" aria-label="Banquet tables set with red napkins" style="background:linear-gradient(135deg,#7a7f85,#b83a3a 55%,#4a4e54)"></div>
  <h4>CONFERENCE #1</h4>
  <div class="meta"><div><span>⚲</span>Riverton, 48 Cedar Lane, USA</div><div><span>▦</span>20/07/2020</div></div>
  <div class="foot">event information</div>
</article>

<h2 class="section-title" style="top:2576px">OUR BLOG</h2>
<div class="underline" style="top:2625px"></div>

<article class="post" style="top:2706px">
  <div class="img" role="img" aria-label="Newspaper front page" style="background:linear-gradient(135deg,#e8e8e8,#6a6a6a)"></div>
  <h4>ADMINISTRATION PROPOSES CUTTING FARM WORKER PAY IN THE MIDST OF A PANDEMIC</h4>
  <p>Lorem ipsum dolor sit amet, consetetur sadipscing elitr, sed diam nonumy eirmod tempor invidunt ut labore et dolore magna aliquyam erat, sed diam voluptua. At vero eos et accusam et justo duo dolores et ea rebum. Stet clita kasd gubergren, no sea takimata sanctus est Lorem ipsum ...</p>
  <div class="more">READ MORE</div><div class="date">Sep 11, 2020</div>
</article>
<article class="post" style="top:2982px">
  <div class="img" role="img" aria-label="Workers at a rally" style="background:linear-gradient(135deg,#5a4035,#b35a4a 50%,#7a8a96)"></div>
  <h4>PROTECT ESSENTIAL FARM WORKERS FROM DEPORTATION, FARM WORKER WILL URGE HOUSE JUDICIARY COMMITTEE</h4>
  <p>Lorem ipsum dolor sit amet, consetetur sadipscing elitr, sed diam nonumy eirmod tempor invidunt ut labore et dolore magna aliquyam erat, sed diam voluptua. At vero eos et accusam et justo duo dolores et ea rebum. Stet clita kasd gubergren, no sea takimata sanctus est Lorem ipsum ...</p>
  <div class="more">READ MORE</div><div class="date">Jul 10, 2020</div>
</article>
<article class="post" style="top:3259px">
  <div class="img" role="img" aria-label="Blue protective gloves on a table" style="background:linear-gradient(135deg,#e9eef2,#2f8ee0 55%,#dfe5ea)"></div>
  <h4>ESSENTIAL WA FARM WORKERS TO RECEIVE MORE SUPPORT AS FIELDHAND FOUNDATION UNVEILS EMERGENCY RELIEF PROGRAM DURING COVID-19</h4>
  <p>Lorem ipsum dolor sit amet, consetetur sadipscing elitr, sed diam nonumy eirmod tempor invidunt ut labore et dolore magna aliquyam erat, sed diam voluptua. At vero eos et accusam et justo duo dolores et ea rebum. Stet clita kasd gubergren, no sea takimata sanctus est Lorem ipsum ...</p>
  <div class="more">READ MORE</div><div class="date">jun 15, 2020</div>
</article>

<div class="btn" style="left:499px;top:3546px;width:200px;height:69px">SEE MORE</div>

<div class="abs dots-area" role="img" aria-label="Decorative dot pattern"></div>
<h3 class="abs support-title">SUPPORT US</h3>
<p class="abs copy support-text">Lorem ipsum dolor sit amet, consetetur sadipscing elitr, sed diam nonumy eirmod tempor invidunt ut labore et dolore magna aliquyam erat, sed diam voluptua. At vero eos et</p>
<div class="btn" style="left:94px;top:3954px;width:199px;height:54px">DONATE</div>
<div class="abs share">share on <b>Chirpline</b><b>Friendbook</b></div>
<div class="abs support-art" role="img" aria-label="Illustration of two people holding a banner with a smiling emblem"></div>

<section class="abs stories">
  <h3>WHY OVER 4,000 PEOPLE TRUST ON US.</h3>
  <article class="story" style="left:-120px;width:478px;opacity:.85">
    <div class="avatar" style="left:110px"></div><div class="name" style="left:195px">Daniel.R</div><div class="ago" style="left:195px">2 days ago - 5min read</div><div class="bm"></div>
    <p style="left:110px;width:340px">Lorem ipsum dolor sit amet, consetetur sadipscing elitr, sed diam nonumy eirmod tempor invidunt ut labore et dolore magna aliquyam erat, sed diam voluptua. At vero eos et accusam et justo duo dolores et ea rebum. Stet</p>
    <div class="loc" style="left:120px">California N</div><div class="likes">♡ 150</div>
  </article>
  <article class="story" style="left:389px;width:458px">
    <div class="avatar"></div><div class="name">Lucia.M</div><div class="ago">5 days ago - 5min read</div><div class="bm"></div>
    <p>Lorem ipsum dolor sit amet, consetetur sadipscing elitr, sed diam nonumy eirmod tempor invidunt ut labore et dolore magna aliquyam erat, sed diam voluptua. At vero eos et accusam et justo duo dolores et ea rebum. Stet clita kasd</p>
    <div class="loc"><b>in</b>California N</div><div class="likes">♡ 500</div>
  </article>
  <article class="story" style="left:869px;width:400px;opacity:.85">
    <div class="avatar"></div><div class="name">Samir.K</div><div class="ago">1 days ago - 5min read</div>
    <p style="width:330px">Lorem ipsum dolor sit amet, consetetur sadipscing elitr, sed diam nonumy eirmod tempor invidunt ut labore et dolore magna aliquyam erat, sed diam voluptua. At vero eos et accusam et justo duo dolores et ea rebum</p>
    <div class="loc"><b>in</b>New york</div>
  </article>
  <div class="pager"><i></i><i></i><i></i><i class="on"></i></div>
</section>

<footer class="abs footer">
  <div class="foot-brand"><span class="dot"></span><span>FIELDHAND<br>FOUNDATION</span></div>
  <span class="social" style="left:424px">Chirpline</span>
  <span class="social" style="left:541px">Friendbook</span>
  <span class="social" style="left:653px">Worknet</span>
  <div class="foot-donate">DONATE US</div>
  <nav class="foot-links"><span>JOIN</span><span>CAREERS</span><span>FIND US ON SOCIAL</span><span>CONTACT US</span><span>PRIVACY PLOLICY</span><span>TERMS AND CONDITIONS</span></nav>
  <div class="copyright">© COPYRIGHT 2020</div>
</footer>

</body>
</html>
```